Lone Prairie Canvas & Sound Jubilee

Organization:
Lone Prairie Canvas and Sound Jubilee is a non-profit organization created by a group of anonymous donors to bring more fun, culture, and art to a small Texas town. Our mission is to promote art and music in Washington County.
The multi-day eclectic festival will feature three stages, a film, art vendors, live mural artists, and food trucks set up throughout historic downtown Brenham. The event is FREE to the public.
Goals:
We need an attractive poster to publicize the festival.
Details:
Lone Prairie Canvas and Sound Jubilee
Friday, October 14 – 16
Free admission (VIP tickets available)
Live music- 3 stages/10 bands
Film Screening
Art vendors and art walk
Live art murals
Food trucks
www.loneprairiecanvasandsoundjubilee.example
#loneprairiecanvasandsound
Requirements:
Please incorporate our festival logo attached.
Conclusion:
After selecting a poster design, we hope to continue to work with the artist to design other event materials including website splash page and rack cards using design elements from the poster.

```html
<!DOCTYPE html>
<html lang="en">
<head>
<meta charset="utf-8">
<title>Lone Prairie Canvas &amp; Sound Jubilee</title>
<link href="https://fonts.googleapis.com/css2?family=Oswald:wght@400;600;700&display=swap" rel="stylesheet">
<style>
  :root {
    --navy: #1b2566;
    --navy-deep: #131c52;
    --pink: #ec2a6e;
    --white: #ffffff;
    --sky: #3fa9f5;
    --sky-deep: #1e6fd9;
  }
  * { margin: 0; padding: 0; box-sizing: border-box; }
  html, body { width: 778px; height: 1200px; overflow: hidden; }
  body {
    font-family: "Oswald", "Arial Narrow", sans-serif;
    background: var(--navy);
    color: var(--white);
  }
  .poster {
    position: relative;
    width: 778px;
    height: 1200px;
    background: radial-gradient(ellipse at 35% 45%, #24307a 0%, var(--navy) 55%, var(--navy-deep) 100%);
    overflow: hidden;
  }
  .clef-art {
    position: absolute;
    left: 120px;
    top: 60px;
    width: 420px;
    height: 1030px;
    border-radius: 210px 210px 180px 180px;
    background: linear-gradient(160deg, var(--sky) 0%, var(--sky-deep) 100%);
    opacity: 0.85;
  }
  .title {
    position: absolute;
    left: 40px;
    top: 44px;
    color: var(--pink);
    font-weight: 700;
    font-size: 64px;
    line-height: 0.98;
    text-transform: uppercase;
    letter-spacing: 0.5px;
  }
  .date {
    position: absolute;
    left: 42px;
    top: 322px;
    font-weight: 600;
    font-size: 22px;
    letter-spacing: 0.5px;
    text-transform: uppercase;
  }
  .highlights {
    position: absolute;
    left: 493px;
    top: 372px;
    list-style: none;
    text-transform: uppercase;
  }
  .highlight { margin-bottom: 22px; }
  .highlight-head {
    display: block;
    font-weight: 700;
    font-size: 44px;
    line-height: 1;
    letter-spacing: 0.5px;
  }
  .highlight-sub {
    display: block;
    font-weight: 400;
    font-size: 20px;
    line-height: 1.3;
    letter-spacing: 1px;
  }
  .venue {
    position: absolute;
    left: 42px;
    top: 1108px;
    text-transform: uppercase;
    font-weight: 600;
    font-size: 20px;
    line-height: 1.2;
  }
  .venue-label { color: var(--white); }
  .venue-place { color: var(--pink); }
  .festival-mark {
    position: absolute;
    left: 540px;
    top: 1010px;
    width: 210px;
    display: flex;
    align-items: center;
    gap: 10px;
    color: var(--pink);
    font-weight: 600;
    font-size: 17px;
    line-height: 1.15;
    text-transform: uppercase;
  }
  .festival-mark-dot {
    flex: none;
    width: 40px;
    height: 40px;
    border-radius: 50%;
    background: var(--pink);
  }
  .contact {
    position: absolute;
    right: 28px;
    top: 1132px;
    text-align: right;
    font-size: 13px;
    font-weight: 400;
    line-height: 1.5;
    text-transform: uppercase;
    letter-spacing: 0.3px;
  }
</style>
</head>
<body>
<main class="poster">
  <div class="clef-art" role="img" aria-label="Large blue treble clef whose lower loop forms an artist's paint palette with red, yellow and green paint dabs, over a faint pattern of music notes"></div>

  <h1 class="title">Lone Prairie<br>Canvas &amp;<br>Sound<br>Jubilee</h1>
  <p class="date">Friday, October 14 – 16</p>

  <ul class="highlights">
    <li class="highlight">
      <span class="highlight-head">Free</span>
      <span class="highlight-sub">Admission</span>
      <span class="highlight-sub">[VIP tickets available]</span>
    </li>
    <li class="highlight">
      <span class="highlight-head">Live Music</span>
      <span class="highlight-sub">3 stages/10 bands</span>
    </li>
    <li class="highlight">
      <span class="highlight-head">Film</span>
      <span class="highlight-sub">Screening</span>
    </li>
    <li class="highlight">
      <span class="highlight-head">Art Vendors</span>
      <span class="highlight-sub">and art walk</span>
    </li>
    <li class="highlight">
      <span class="highlight-head">Live</span>
      <span class="highlight-sub">Art murals</span>
    </li>
    <li class="highlight">
      <span class="highlight-head">Food</span>
      <span class="highlight-sub">Trucks</span>
    </li>
  </ul>

  <div class="festival-mark">
    <span class="festival-mark-dot"></span>
    <span class="festival-mark-name">Lone Prairie Canvas &amp; Sound Jubilee</span>
  </div>

  <div class="venue">
    <div class="venue-label">Venue</div>
    <div class="venue-place">Brenham, TX</div>
  </div>

  <div class="contact">
    <div>www.loneprairiecanvasandsoundjubilee.example</div>
    <div>#loneprairiecanvasandsound</div>
  </div>
</main>
</body>
</html>
```